Bref créative
Brochure for Professional Services Firm
Brightfen Partners
We need a great design for a brochure to be used as marketing collateral at tradeshows and for general marketing purposes. Our website is brightfenpartners.example to get additional information. We generally work with oilfield service companies.
Consulting
Corporate, professional.
===========Update==========
Requirement : Trifold
Our logo files.
Here is a sample presentation we currently use to market our services.
Some stock photos we have.
stock photos.
stock photo.

```html
<!DOCTYPE html>
<html lang="en">
<head>
<meta charset="utf-8">
<title>Brightfen Partners – Services Brochure Panel</title>
<link rel="stylesheet" href="https://fonts.googleapis.com/css2?family=Roboto+Condensed:ital,wght@0,400;0,700;1,700&family=PT+Serif:wght@400;700&display=swap">
<style>
  :root {
    --backdrop: #c9cacc;
    --paper: #ffffff;
    --brand-blue: #1e9ad6;
    --brand-blue-dark: #1580b8;
    --navy: #1c2836;
    --navy-soft: #2c3a4b;
    --text: #2b2f33;
    --muted: #5a6068;
    --photo-sky: #3f78b8;
    --photo-steel: #1d2530;
  }
  * { box-sizing: border-box; margin: 0; padding: 0; }
  html, body { width: 1200px; height: 799px; overflow: hidden; }
  body {
    background: var(--backdrop);
    font-family: "PT Serif", Georgia, serif;
    color: var(--text);
  }
  .brochure-panel {
    position: absolute;
    left: 150px; top: 40px;
    width: 900px; height: 719px;
    background: var(--paper);
    box-shadow: 0 6px 24px rgba(0,0,0,.18);
    overflow: hidden;
  }
  .hero-photo {
    position: absolute; left: 0; top: 0;
    width: 900px; height: 250px;
    background: linear-gradient(160deg, var(--photo-sky) 0%, #6d9fd2 40%, #3a4f66 70%, var(--photo-steel) 100%);
  }
  .tagline-band {
    position: absolute; left: 0; top: 168px;
    width: 520px; height: 66px;
    background: rgba(28,40,54,.92);
    clip-path: polygon(0 0, 100% 0, 94% 100%, 0 100%);
    display: flex; align-items: center; gap: 18px;
    padding: 0 40px 0 22px;
  }
  .tagline-title {
    font-family: "Roboto Condensed", Arial, sans-serif;
    font-weight: 700; font-size: 21px; line-height: 1.05;
    color: var(--brand-blue); width: 170px;
  }
  .tagline-text {
    font-size: 11px; line-height: 1.35; color: #e3e8ee; width: 270px;
  }
  .accent-stripe {
    position: absolute; left: 0; top: 250px;
    width: 900px; height: 8px; background: var(--brand-blue);
  }
  .section-header {
    position: absolute; left: 22px; top: 282px;
    display: flex; align-items: center; gap: 12px;
  }
  .section-title {
    font-family: "Roboto Condensed", Arial, sans-serif;
    font-weight: 700; font-size: 38px; letter-spacing: .5px;
    color: var(--brand-blue);
  }
  .section-intro {
    font-size: 14px; line-height: 1.3; color: var(--muted);
    width: 330px; padding-left: 14px; border-left: 2px solid var(--brand-blue);
  }
  .service-grid {
    position: absolute; left: 22px; top: 358px;
    width: 856px;
    display: grid; grid-template-columns: repeat(3, 1fr); gap: 22px;
  }
  .service-card { display: flex; flex-direction: column; }
  .service-photo {
    height: 78px; width: 100%;
    background: linear-gradient(180deg, #9fb6cc 0%, #6e7f92 60%, #3c4652 100%);
  }
  .service-photo.fleet { background: linear-gradient(180deg, #b9c6d2 0%, #8d99a5 55%, #4a525c 100%); }
  .service-photo.gears { background: linear-gradient(180deg, #e4e8ec 0%, #a9b3bd 55%, #5f6a76 100%); }
  .service-label {
    margin-top: 8px; height: 26px;
    background: var(--brand-blue);
    display: flex; align-items: center; padding-left: 10px;
    font-family: "Roboto Condensed", Arial, sans-serif;
    font-weight: 700; font-style: italic; font-size: 14px; color: #fff;
  }
  .service-text {
    margin-top: 10px; font-size: 11.5px; line-height: 1.5;
    color: var(--text); text-align: justify;
  }
  .service-list {
    margin-top: 8px; font-size: 11.5px; line-height: 1.5; color: var(--brand-blue-dark);
  }
  .footer-band {
    position: absolute; left: 0; bottom: 0;
    width: 900px; height: 46px; background: var(--navy);
    display: flex; align-items: center; justify-content: space-between; padding: 0 22px;
  }
  .footer-name {
    font-family: "Roboto Condensed", Arial, sans-serif;
    font-weight: 700; font-size: 14px; letter-spacing: 1px; color: #fff;
  }
</style>
</head>
<body>
  <article class="brochure-panel">
    <div class="hero-photo" role="img" aria-label="Oilfield wellhead pipes and valves against a blue sky"></div>
    <div class="tagline-band">
      <h2 class="tagline-title">We are a small firm by design</h2>
      <p class="tagline-text">A decision to stay small and focus on a number of key engagements allows us to provide the personal attention our clients expect.</p>
    </div>
    <div class="accent-stripe"></div>

    <header class="section-header">
      <svg width="46" height="28" viewBox="0 0 46 28" aria-hidden="true">
        <polygon points="0,0 12,0 24,14 12,28 0,28 12,14" fill="var(--brand-blue)"/>
        <polygon points="18,0 30,0 42,14 30,28 18,28 30,14" fill="var(--brand-blue)"/>
      </svg>
      <h1 class="section-title">SERVICES</h1>
      <p class="section-intro">Boutique financial and transaction advisory services for small and mid-market companies.</p>
    </header>

    <section class="service-grid">
      <div class="service-card">
        <div class="service-photo" role="img" aria-label="Industrial pipeline equipment at a field site"></div>
        <h3 class="service-label">Transaction Advisory Services</h3>
        <p class="service-text">We have worked through several transactions and know what it takes to get a deal closed. We also know how costly incorrect advice can be when owners are distracted from managing their core business. At Brightfen, we work hard to keep each deal on track and moving forward. We quickly integrate with your team and stay with the entire transaction process.</p>
      </div>
      <div class="service-card">
        <div class="service-photo fleet" role="img" aria-label="Tanker trucks lined up at an oilfield service yard"></div>
        <h3 class="service-label">Financial Advisory Services</h3>
        <p class="service-text">The financial due diligence process is one aspect of a transaction that many business owners are not ready for. Our team helps prepare management for the questions buyers will ask, and guides the process through every stage. A thorough review of the numbers protects value and keeps surprises to a minimum.</p>
      </div>
      <div class="service-card">
        <div class="service-photo gears" role="img" aria-label="Close view of machined steel gears"></div>
        <h3 class="service-label">CFO Consulting Services</h3>
        <p class="service-text">Whether your business requires a part-time CFO or a full-time interim leader, Brightfen Partners works with you to ensure you have the strategic and financial guidance your company needs. Brightfen Partners offers CFO consulting services.</p>
        <p class="service-list">Part-time CFO services | Internal audit | Interim CFO services</p>
      </div>
    </section>

    <footer class="footer-band">
      <svg width="90" height="20" viewBox="0 0 90 20" aria-hidden="true">
        <polygon points="0,0 9,0 18,10 9,20 0,20 9,10" fill="var(--brand-blue)"/>
        <polygon points="24,0 33,0 42,10 33,20 24,20 33,10" fill="var(--brand-blue)"/>
        <polygon points="48,0 57,0 66,10 57,20 48,20 57,10" fill="var(--navy-soft)"/>
      </svg>
      <span class="footer-name">BRIGHTFEN PARTNERS</span>
    </footer>
  </article>
</body>
</html>
```